Nightclub promoter business cards

We need business cards designed for our company based in Toronto, Canada called "NowMirazo". We are an events company that promotes weekly parties in the city. We cater to a 25+ crowd and feel like our brand should reflect that. We are looking for business cards that are textured and contain a unique design. We would prefer black cards. The final design should communicate the finest hospitality and prestige. I've attached files containing our logo. For more info. about our brand visit our website at www.nowmirazo.example.

Industry/Entity Type

Business

```html
<!DOCTYPE html>
<html lang="en">
<head>
<meta charset="utf-8">
<title>NowMirazo Business Cards</title>
<link rel="stylesheet" href="https://fonts.googleapis.com/css2?family=Josefin+Sans:wght@300;600&display=swap">
<style>
  :root {
    --page: #ffffff;
    --card-dark: #1c1c1d;
    --card-mid: #2b2b2c;
    --card-glow: #5a5a5c;
    --card-edge: #8a8a8c;
    --ink-light: #ffffff;
    --ink-soft: #e4e4e4;
    --wave-deep: #0a0a0a;
    --wave-sheen: #3a3a3b;
  }
  html, body {
    margin: 0;
    padding: 0;
    width: 1200px;
    height: 927px;
    overflow: hidden;
    background: var(--page);
  }
  .sheet {
    position: relative;
    width: 1200px;
    height: 927px;
  }
  .card {
    position: absolute;
    box-sizing: border-box;
    border-radius: 18px;
    overflow: hidden;
  }
  .card--front {
    left: 87px;
    top: 45px;
    width: 573px;
    height: 362px;
    background: radial-gradient(circle at 35% 45%, var(--card-glow) 0%, var(--card-mid) 38%, var(--card-dark) 75%);
  }
  .card--back {
    left: 516px;
    top: 463px;
    width: 578px;
    height: 364px;
    border: 2px solid var(--card-edge);
    background: radial-gradient(circle at 47% 18%, var(--card-glow) 0%, var(--card-mid) 32%, var(--card-dark) 70%);
  }
  .wordmark {
    position: absolute;
    right: 40px;
    bottom: 48px;
    margin: 0;
    font-family: "Josefin Sans", sans-serif;
    font-weight: 600;
    font-size: 70px;
    line-height: 1;
    letter-spacing: -1px;
    color: var(--ink-light);
  }
  .contact {
    position: absolute;
    left: 40px;
    top: 53px;
    margin: 0;
    font-family: "Josefin Sans", sans-serif;
    font-weight: 300;
    font-style: normal;
    font-size: 18px;
    line-height: 28px;
    color: var(--ink-soft);
  }
  .contact span { display: block; }
  .wave-art {
    position: absolute;
    left: 0;
    bottom: 0;
    width: 100%;
    height: 230px;
  }
</style>
</head>
<body>
  <main class="sheet">
    <section class="card card--front" aria-label="Card front">
      <h1 class="wordmark">nowmirazo</h1>
    </section>

    <section class="card card--back" aria-label="Card back">
      <address class="contact">
        <span class="contact__name">Name</span>
        <span class="contact__web">www.nowmirazo.example</span>
        <span class="contact__phone">555-010-4289</span>
      </address>
      <svg class="wave-art" viewBox="0 0 578 230" preserveAspectRatio="none" role="img" aria-label="Flowing dark ribbon swirls across the lower card">
        <defs>
          <linearGradient id="waveFill" x1="0" y1="0" x2="0" y2="1">
            <stop offset="0" stop-color="#1c1c1d" stop-opacity="0"/>
            <stop offset="0.45" stop-color="var(--wave-sheen)" stop-opacity="0.55"/>
            <stop offset="0.7" stop-color="var(--wave-deep)" stop-opacity="0.9"/>
            <stop offset="1" stop-color="#242425" stop-opacity="0.8"/>
          </linearGradient>
        </defs>
        <rect x="0" y="0" width="578" height="230" fill="url(#waveFill)"/>
      </svg>
    </section>
  </main>
</body>
</html>
```